R4 Pips (CBD candy infused with Delta-8)

The proposed logo are two pool table balls. One is a D and the other is an 8, its a brand and we need a label for Gummy human treats. This treats are being infused with Delt-8. I i will upload examples only. The example is of the type of labels needed (package and label for bottle)

Target Market(s)

Your professionals

Font styles to use
Sans Serif

Requirements
Must have
• Youthful look
Nice to have
• Consider using the Delta symbol instead of the D.
Also, I provided a sample of a label that's used on two type of packages.

```html
<!DOCTYPE html>
<html lang="en">
<head>
<meta charset="utf-8">
<title>R4 Pips Gummy Human Treats Label</title>
<link rel="stylesheet" href="https://fonts.googleapis.com/css2?family=Fredoka:wght@600;700&family=Nunito+Sans:wght@800&display=swap">
<style>
  :root {
    --page: #ffffff;
    --seal-red: #d13236;
    --label-white: #f1f1f1;
    --navy: #2b3a5a;
    --gold: #e3c35a;
    --brand-brown: #5b3b42;
    --ball-red: #d8353a;
    --text-dark: #3a3a3a;
    --candy-a: #e8602a;
    --candy-b: #f0b43a;
    --candy-c: #3f9a3a;
    --candy-d: #d83a3a;
  }
  html, body {
    margin: 0;
    width: 1200px;
    height: 1200px;
    overflow: hidden;
    background: var(--page);
  }
  .canvas {
    position: relative;
    width: 1200px;
    height: 1200px;
  }
  .pouch {
    position: absolute;
    left: 354px;
    top: 212px;
    width: 500px;
    height: 788px;
    background: var(--label-white);
    overflow: hidden;
  }
  .seal-band {
    position: absolute;
    left: 0; top: 0;
    width: 100%;
    height: 125px;
    background: var(--seal-red);
    border-bottom: 4px solid var(--gold);
  }
  .brand {
    position: absolute;
    left: 0; top: 150px;
    width: 100%;
    display: flex;
    flex-direction: column;
    align-items: center;
  }
  .brand-dot {
    width: 140px;
    height: 140px;
    border-radius: 50%;
    background: var(--ball-red);
  }
  .brand-name {
    margin-top: 12px;
    font-family: "Fredoka", sans-serif;
    font-weight: 600;
    font-size: 62px;
    line-height: 1;
    color: var(--brand-brown);
  }
  .product-band {
    position: absolute;
    left: 0; top: 0;
    width: 500px;
    height: 788px;
  }
  .product-title {
    position: absolute;
    left: 0; top: 432px;
    width: 100%;
    text-align: center;
    font-family: "Fredoka", sans-serif;
    font-weight: 700;
    color: #ffffff;
    line-height: 1;
  }
  .product-title .main {
    display: block;
    font-size: 84px;
    letter-spacing: 2px;
  }
  .product-title .sub {
    display: block;
    margin-top: 8px;
    font-size: 46px;
    letter-spacing: 2px;
  }
  .net-weight {
    position: absolute;
    left: 0; top: 656px;
    width: 100%;
    text-align: center;
    font-family: "Nunito Sans", sans-serif;
    font-weight: 800;
    font-size: 22px;
    color: var(--text-dark);
  }
  .candy-strip {
    position: absolute;
    left: 0; top: 694px;
    width: 100%;
    height: 94px;
    border-top: 4px solid var(--gold);
    background: linear-gradient(90deg, var(--candy-d), var(--candy-c) 18%, var(--candy-a) 35%, var(--candy-b) 55%, var(--candy-c) 70%, var(--candy-a) 85%, var(--candy-b));
  }
</style>
</head>
<body>
<main class="canvas">
  <section class="pouch">
    <div class="seal-band"></div>

    <div class="brand">
      <div class="brand-dot"></div>
      <div class="brand-name">R4 Pips</div>
    </div>

    <svg class="product-band" viewBox="0 0 500 788" aria-hidden="true">
      <path d="M0 388 Q250 468 500 388 L500 625 Q250 581 0 625 Z" fill="var(--navy)"/>
      <path d="M0 388 Q250 468 500 388" fill="none" stroke="var(--gold)" stroke-width="5"/>
      <path d="M0 625 Q250 581 500 625" fill="none" stroke="var(--gold)" stroke-width="5"/>
    </svg>

    <h1 class="product-title">
      <span class="main">GUMMY</span>
      <span class="sub">HUMAN TREATS</span>
    </h1>

    <div class="net-weight">Net Wt. 250g.</div>

    <div class="candy-strip" role="img" aria-label="Photo of colourful gummy bears"></div>
  </section>
</main>
</body>
</html>
```